Social

We are seeking a skilled designer to create a set of visually compelling social media ad creatives that will drive traffic to our Wood Look Paver landing page, encouraging visitors to download our brochure.
Landing page: https://veltrano.com/wood-look-porcelain-paver-solutions-downloadable-guide/
The broader campaign is focused on educating architects, contractors, and homeowners on the availability and advantages of wood look porcelain pavers as an alternative to natural wood. Ads will highlight both real-world installation images and available wood sample colors to spark interest and drive click-throughs.
Scope:
Design 3 ad sets with distinct styling and copy concepts.
Ads should align with platform best practices for:
Facebook
Instagram
LinkedIn
See brief for sizing.
Creative Direction:
Use installation photos and wood sample color swatches as primary visuals.
Design should clearly highlight the brochure download call-to-action.
Visual style should balance modern and professional, appealing to both design professionals and homeowners.
Target Market(s)
Architects
Industry/Entity Type
Construction
Font styles to use
Other font styles liked:
- Outfit, Helvetica (other fonts are possible)
Look and feel
Each slider illustrates characteristics of the customer's brand and the style your logo design should communicate.

```html
<!DOCTYPE html>
<html lang="en">
<head>
<meta charset="utf-8">
<title>Veltrano – Wood Look Porcelain Pavers Social Ads</title>
<link rel="stylesheet" href="https://fonts.googleapis.com/css2?family=Outfit:wght@300;400;500;700;800&family=Oswald:wght@600;700&family=Roboto+Condensed:wght@300;400&display=swap">
<style>
  :root{
    --ink:#1b1b1b;
    --teal:#0e7f89;
    --teal-deep:#0b6f78;
    --teal-sky:#3db0cc;
    --yellow:#f8cf16;
    --paper:#f5f8f9;
    --white:#ffffff;
    --grey-band:#efefef;
    --wood-dark:#7f5238;
    --wood-mid:#a4754f;
    --wood-light:#bba68a;
    --wood-grey:#cfcdc7;
    --wood-warm:#9b7a5e;
  }
  *{box-sizing:border-box;margin:0;padding:0}
  html,body{width:1200px;height:3000px;overflow:hidden;background:var(--white)}
  body{position:relative;font-family:"Outfit",Helvetica,Arial,sans-serif;color:var(--ink)}

  .ad-set{position:absolute;left:0;width:1200px;height:1000px}
  .ad-set--light{top:0;background:var(--white)}
  .ad-set--grey{top:1000px;background:var(--grey-band)}
  .ad-set--fire{top:2000px;background:var(--white)}

  .ad{position:absolute;overflow:hidden}
  .ad--story{left:203px;top:118px;width:430px;height:764px}
  .ad--portrait{left:682px;top:118px;width:315px;height:393px}
  .ad--square{left:682px;top:567px;width:315px;height:315px}

  .ad--paper{background:var(--paper)}
  .ad--teal{background:linear-gradient(180deg,var(--teal-deep) 0%,#1f8f9e 45%,var(--teal-sky) 100%)}
  .ad--fire{background:linear-gradient(180deg,var(--teal-deep) 0%,#1a8791 40%,#5fa9b3 62%,#cdb89c 100%)}

  .brand{position:absolute;display:flex;align-items:center;gap:.3em;font-weight:400;letter-spacing:.01em;white-space:nowrap}
  .brand__mark{width:.72em;height:.72em;background:currentColor;display:block}
  .brand--dark{color:var(--ink)}
  .brand--dark .brand__mark{background:var(--teal)}
  .brand--light{color:var(--white)}

  .headline{position:absolute;font-weight:400;line-height:.92;letter-spacing:-.01em}
  .headline .accent{color:var(--teal)}
  .headline .gold{color:var(--yellow)}
  .headline--right{text-align:right}
  .headline--white{color:var(--white)}

  .lede{position:absolute;font-family:"Roboto Condensed",Helvetica,Arial,sans-serif;font-weight:300;line-height:1.28}
  .lede--white{color:var(--white);text-align:right}

  .cta{position:absolute;display:flex;align-items:center;justify-content:center;font-family:"Oswald",Helvetica,Arial,sans-serif;font-weight:700;text-transform:uppercase;letter-spacing:.01em;border-radius:6px;white-space:nowrap}
  .cta--yellow{background:var(--yellow);color:var(--ink)}
  .cta--fire{background:var(--yellow);color:var(--teal-deep)}
  .cta--teal{background:var(--teal-deep);color:var(--yellow);border-radius:10px}

  .photo{position:absolute;display:block}
  .photo--patio{background:linear-gradient(180deg,rgba(245,248,249,0) 0%,#5b7a45 28%,#3f5e33 58%,#a99a84 82%,#c9bba5 100%)}
  .photo--wall{background:linear-gradient(90deg,#d8d2c6 0%,#ece8e0 40%,#b5b0a6 60%,#3c3f3c 100%)}

  .swatch{position:absolute;border-radius:50%;display:block}
  .swatch--ring{border:3px solid var(--white)}
  .sw-dark{background:radial-gradient(circle at 40% 35%,#9a6a4c,var(--wood-dark))}
  .sw-mid{background:radial-gradient(circle at 40% 35%,#b98a62,var(--wood-mid))}
  .sw-light{background:radial-gradient(circle at 40% 35%,#cbb99c,var(--wood-light))}
  .sw-grey{background:radial-gradient(circle at 40% 35%,#e2e0db,var(--wood-grey))}
  .sw-warm{background:radial-gradient(circle at 40% 35%,#b3947a,var(--wood-warm))}

  .styles-count{position:absolute;color:var(--white);text-align:left;line-height:.9}
  .styles-count__num{font-weight:400;position:relative;display:inline-block}
  .styles-count__plus{position:absolute;top:.05em;right:-.55em;width:.5em;height:.5em;border-radius:50%;background:var(--yellow);color:var(--teal-deep);font-size:.5em;line-height:1;display:flex;align-items:center;justify-content:center;font-weight:700}
  .styles-count__label{display:block;font-weight:300;letter-spacing:.02em}

  .scene{position:absolute;left:0;top:0}

  .fire-build{position:absolute;color:var(--white);font-weight:400;line-height:1}
  .fire-pct{position:absolute;color:var(--yellow);font-weight:800;line-height:1;letter-spacing:-.04em}
  .fire-decks{position:absolute;color:var(--white);font-weight:300;line-height:1}
  .fire-note{position:absolute;color:var(--white);font-family:"Roboto Condensed",Helvetica,Arial,sans-serif;font-weight:300;line-height:1.25;border-left:2px solid var(--yellow)}
  .photo--deck{background:linear-gradient(180deg,rgba(95,169,179,0) 0%,#9db3b3 22%,#8f8a80 45%,#c9b595 70%,#d9c7a8 100%)}
</style>
</head>
<body>

<!-- Ad set 1: light paper style -->
<section class="ad-set ad-set--light">

  <article class="ad ad--story ad--paper">
    <span class="photo photo--patio" style="left:0;top:420px;width:430px;height:344px" role="img" aria-label="Installation photo: garden terrace with wood look porcelain pavers, outdoor lounge and trees"></span>
    <span class="photo photo--wall" style="left:320px;top:440px;width:110px;height:324px" role="img" aria-label="Modern house wall with large glass windows"></span>
    <div class="brand brand--dark" style="left:48px;top:58px;font-size:25px"><span class="brand__mark"></span>Veltrano</div>
    <h1 class="headline" style="left:44px;top:128px;font-size:58px">Wood Look<br><span class="accent">Porcelain<br>Pavers</span></h1>
    <p class="lede" style="left:44px;top:308px;font-size:17px">The warmth of<br>natural wood,<br>the advantages<br>of porcelain.</p>
    <div class="cta cta--yellow" style="left:26px;top:415px;width:186px;height:34px;font-size:16px">Download the guide</div>
    <span class="swatch sw-dark" style="left:260px;top:281px;width:88px;height:88px" role="img" aria-label="Dark wood sample"></span>
    <span class="swatch sw-mid" style="left:329px;top:346px;width:78px;height:78px" role="img" aria-label="Medium wood sample"></span>
    <span class="swatch sw-light" style="left:256px;top:376px;width:72px;height:72px" role="img" aria-label="Light wood sample"></span>
  </article>

  <article class="ad ad--portrait ad--paper">
    <span class="photo photo--patio" style="left:0;top:240px;width:315px;height:153px" role="img" aria-label="Installation photo: garden terrace with wood look porcelain pavers"></span>
    <span class="photo photo--wall" style="left:215px;top:200px;width:100px;height:193px" role="img" aria-label="Modern house wall with glass windows"></span>
    <div class="brand brand--dark" style="right:22px;top:20px;font-size:13px"><span class="brand__mark"></span>Veltrano</div>
    <h2 class="headline" style="left:30px;top:42px;font-size:34px">Wood<br>Look<br><span class="accent">Porcelain<br>Pavers</span></h2>
    <p class="lede" style="left:30px;top:176px;font-size:10px">The warmth of natural wood,<br>the advantages of porcelain.</p>
    <div class="cta cta--yellow" style="left:24px;top:220px;width:135px;height:24px;font-size:11px">Download the guide</div>
    <span class="swatch sw-dark" style="left:200px;top:79px;width:62px;height:62px" role="img" aria-label="Dark wood sample"></span>
    <span class="swatch sw-mid" style="left:247px;top:124px;width:54px;height:54px" role="img" aria-label="Medium wood sample"></span>
    <span class="swatch sw-light" style="left:198px;top:144px;width:50px;height:50px" role="img" aria-label="Light wood sample"></span>
  </article>

  <article class="ad ad--square ad--paper">
    <span class="photo photo--patio" style="left:0;top:180px;width:315px;height:135px" role="img" aria-label="Installation photo: garden terrace with wood look porcelain pavers"></span>
    <span class="photo photo--wall" style="left:205px;top:140px;width:110px;height:175px" role="img" aria-label="Modern house wall with glass windows"></span>
    <div class="brand brand--dark" style="left:30px;top:18px;font-size:11px"><span class="brand__mark"></span>Veltrano</div>
    <h2 class="headline" style="left:30px;top:50px;font-size:31px">Wood<br>Look<br><span class="accent">Porcelain<br>Pavers</span></h2>
    <p class="lede" style="left:30px;top:166px;font-size:8.5px">The warmth of natural wood,<br>the advantages of porcelain.</p>
    <span class="swatch sw-dark" style="left:188px;top:16px;width:68px;height:68px" role="img" aria-label="Dark wood sample"></span>
    <span class="swatch sw-mid" style="left:240px;top:64px;width:58px;height:58px" role="img" aria-label="Medium wood sample"></span>
    <span class="swatch sw-light" style="left:188px;top:86px;width:52px;height:52px" role="img" aria-label="Light wood sample"></span>
    <div class="cta cta--yellow" style="left:168px;top:266px;width:147px;height:26px;font-size:11px;border-radius:6px 0 0 6px">Download the guide</div>
  </article>
</section>

<!-- Ad set 2: teal with curved photo -->
<section class="ad-set ad-set--grey">

  <article class="ad ad--story ad--teal">
    <svg class="scene" width="430" height="764" viewBox="0 0 430 764" role="img" aria-label="Installation photo: modern house terrace with wood look porcelain planks and sea view">
      <defs>
        <linearGradient id="terraceA" x1="0" y1="0" x2="0" y2="1">
          <stop offset="0" stop-color="#5d7d80"/>
          <stop offset=".45" stop-color="#4a4a40"/>
          <stop offset=".7" stop-color="#8a6a52"/>
          <stop offset="1" stop-color="#a07c60"/>
        </linearGradient>
      </defs>
      <path d="M0 280 L430 180 L430 540 C 370 560 320 690 200 690 C 110 690 50 640 0 500 Z" fill="url(#terraceA)"/>
      <path d="M0 500 C 50 640 110 690 200 690 C 320 690 370 560 430 540" fill="none" stroke="#fff" stroke-width="8"/>
    </svg>
    <div class="brand brand--light" style="right:40px;top:58px;font-size:21px"><span class="brand__mark"></span>Veltrano</div>
    <h2 class="headline headline--right headline--white" style="right:40px;top:96px;font-size:43px;line-height:.9"><span class="gold">Wood Look</span><br>Porcelain Pavers<br>and Planks</h2>
    <p class="lede lede--white" style="right:40px;top:234px;font-size:15px">The rich details of wood,<br>the advantages of porcelain</p>
    <div class="cta cta--yellow" style="left:229px;top:294px;width:171px;height:38px;font-size:18px;border-radius:8px">Order a sample</div>
    <span class="swatch swatch--ring sw-dark" style="left:20px;top:540px;width:76px;height:76px" role="img" aria-label="Dark wood sample"></span>
    <span class="swatch swatch--ring sw-grey" style="left:78px;top:618px;width:74px;height:74px" role="img" aria-label="Grey wood sample"></span>
    <span class="swatch swatch--ring sw-warm" style="left:176px;top:611px;width:74px;height:74px" role="img" aria-label="Warm wood sample"></span>
    <span class="swatch swatch--ring sw-grey" style="left:258px;top:574px;width:74px;height:74px" role="img" aria-label="Light grey wood sample"></span>
    <span class="swatch swatch--ring sw-light" style="left:342px;top:534px;width:72px;height:72px" role="img" aria-label="Light wood sample"></span>
    <div class="styles-count" style="left:314px;top:672px;font-size:48px"><span class="styles-count__num">20<span class="styles-count__plus">+</span></span><span class="styles-count__label" style="font-size:24px">STYLES</span></div>
  </article>

  <article class="ad ad--portrait ad--teal">
    <svg class="scene" width="315" height="393" viewBox="0 0 315 393" role="img" aria-label="Installation photo: modern house terrace with wood look porcelain planks">
      <defs>
        <linearGradient id="terraceB" x1="0" y1="0" x2="0" y2="1">
          <stop offset="0" stop-color="#5d7d80"/>
          <stop offset=".5" stop-color="#4a4a40"/>
          <stop offset="1" stop-color="#a07c60"/>
        </linearGradient>
      </defs>
      <path d="M0 0 L160 0 L180 240 L315 250 L315 280 C 260 300 200 370 120 370 C 60 370 25 320 0 270 Z" fill="url(#terraceB)"/>
      <path d="M0 270 C 25 320 60 370 120 370 C 200 370 260 300 315 280" fill="none" stroke="#fff" stroke-width="5"/>
    </svg>
    <div class="brand brand--light" style="right:18px;top:20px;font-size:13px"><span class="brand__mark"></span>Veltrano</div>
    <h2 class="headline headline--right headline--white" style="right:30px;top:46px;font-size:27px;line-height:.88"><span class="gold">Wood Look</span><br>Porcelain Pavers<br>and Planks</h2>
    <p class="lede lede--white" style="right:30px;top:146px;font-size:9.5px;line-height:1.5">The rich details<br>of wood,<br>the advantages<br>of porcelain</p>
    <div class="cta cta--yellow" style="left:180px;top:227px;width:120px;height:25px;font-size:11px">Order a sample</div>
    <span class="swatch swatch--ring sw-dark" style="left:14px;top:265px;width:56px;height:56px" role="img" aria-label="Dark wood sample"></span>
    <span class="swatch swatch--ring sw-grey" style="left:55px;top:325px;width:54px;height:54px" role="img" aria-label="Grey wood sample"></span>
    <span class="swatch swatch--ring sw-warm" style="left:128px;top:318px;width:54px;height:54px" role="img" aria-label="Warm wood sample"></span>
    <span class="swatch swatch--ring sw-grey" style="left:188px;top:285px;width:54px;height:54px" role="img" aria-label="Light grey wood sample"></span>
    <span class="swatch swatch--ring sw-light" style="left:250px;top:267px;width:52px;height:52px" role="img" aria-label="Light wood sample"></span>
    <div class="styles-count" style="left:240px;top:334px;font-size:30px"><span class="styles-count__num">20<span class="styles-count__plus">+</span></span><span class="styles-count__label" style="font-size:14px">STYLES</span></div>
  </article>

  <article class="ad ad--square ad--teal">
    <svg class="scene" width="315" height="315" viewBox="0 0 315 315" role="img" aria-label="Installation photo: modern house terrace with wood look porcelain planks">
      <defs>
        <linearGradient id="terraceC" x1="0" y1="0" x2="0" y2="1">
          <stop offset="0" stop-color="#5d7d80"/>
          <stop offset=".5" stop-color="#4a4a40"/>
          <stop offset="1" stop-color="#a07c60"/>
        </linearGradient>
      </defs>
      <path d="M0 0 L160 0 L180 200 L315 200 L315 225 C 260 240 210 300 130 300 C 60 300 25 250 0 200 Z" fill="url(#terraceC)"/>
      <path d="M0 200 C 25 250 60 300 130 300 C 210 300 260 240 315 225" fill="none" stroke="#fff" stroke-width="5"/>
    </svg>
    <div class="brand brand--light" style="right:18px;top:20px;font-size:11px"><span class="brand__mark"></span>Veltrano</div>
    <h2 class="headline headline--right headline--white" style="right:18px;top:40px;font-size:25px;line-height:.88"><span class="gold">Wood Look</span><br>Porcelain Pavers<br>and Planks</h2>
    <p class="lede lede--white" style="right:18px;top:128px;font-size:8.5px;line-height:1.5">The rich details of wood,<br>the advantages<br>of porcelain</p>
    <div class="cta cta--yellow" style="left:188px;top:190px;width:127px;height:24px;font-size:11px;border-radius:6px 0 0 6px">Order a sample</div>
    <span class="swatch swatch--ring sw-dark" style="left:12px;top:162px;width:44px;height:44px" role="img" aria-label="Dark wood sample"></span>
    <span class="swatch swatch--ring sw-grey" style="left:38px;top:214px;width:42px;height:42px" role="img" aria-label="Grey wood sample"></span>
    <span class="swatch swatch--ring sw-warm" style="left:78px;top:250px;width:44px;height:44px" role="img" aria-label="Warm wood sample"></span>
    <span class="swatch swatch--ring sw-dark" style="left:136px;top:256px;width:42px;height:42px" role="img" aria-label="Dark wood sample"></span>
    <span class="swatch swatch--ring sw-grey" style="left:190px;top:236px;width:44px;height:44px" role="img" aria-label="Light grey wood sample"></span>
    <div class="styles-count" style="left:246px;top:262px;font-size:28px"><span class="styles-count__num">20<span class="styles-count__plus">+</span></span><span class="styles-count__label" style="font-size:13px">STYLES</span></div>
  </article>
</section>

<!-- Ad set 3: fireproof decks -->
<section class="ad-set ad-set--fire">

  <article class="ad ad--story ad--fire">
    <span class="photo photo--deck" style="left:0;top:380px;width:430px;height:384px" role="img" aria-label="Installation photo: poolside deck with wood look porcelain pavers, lounge chairs and stucco house by the sea"></span>
    <div class="brand brand--light" style="right:38px;top:48px;font-size:24px"><span class="brand__mark"></span>Veltrano</div>
    <div class="fire-build" style="left:38px;top:90px;font-size:72px">Build</div>
    <div class="fire-pct" style="left:26px;top:155px;font-size:118px">100%</div>
    <div class="fire-decks" style="left:40px;top:280px;font-size:38px">Fireproof Decks</div>
    <p class="fire-note" style="left:40px;top:339px;font-size:18px;padding-left:12px">On-grade or elevated on<br>steel pedestals</p>
    <div class="cta cta--teal" style="left:117px;top:666px;width:196px;height:52px;font-size:25px">Learn more</div>
  </article>

  <article class="ad ad--portrait ad--fire">
    <span class="photo photo--deck" style="left:0;top:160px;width:315px;height:233px" role="img" aria-label="Installation photo: poolside deck with wood look porcelain pavers and stucco house"></span>
    <div class="brand brand--light" style="right:18px;top:18px;font-size:13px"><span class="brand__mark"></span>Veltrano</div>
    <div class="fire-build" style="left:28px;top:34px;font-size:48px">Build</div>
    <div class="fire-pct" style="left:18px;top:76px;font-size:78px">100%</div>
    <div class="fire-decks" style="left:28px;top:158px;font-size:26px">Fireproof Decks</div>
    <p class="fire-note" style="left:28px;top:190px;font-size:10px;padding-left:8px">On-grade or elevated on<br>steel pedestals</p>
    <div class="cta cta--fire" style="left:20px;top:336px;width:135px;height:34px;font-size:17px">Learn more</div>
  </article>

  <article class="ad ad--square ad--fire">
    <span class="photo photo--deck" style="left:0;top:120px;width:315px;height:195px" role="img" aria-label="Installation photo: poolside deck with wood look porcelain pavers and stucco house"></span>
    <div class="brand brand--light" style="right:22px;top:18px;font-size:13px"><span class="brand__mark"></span>Veltrano</div>
    <div class="fire-build" style="left:28px;top:28px;font-size:40px">Build</div>
    <div class="fire-pct" style="left:20px;top:62px;font-size:66px">100%</div>
    <div class="fire-decks" style="left:28px;top:128px;font-size:22px">Fireproof Decks</div>
    <p class="fire-note" style="left:35px;top:270px;font-size:9px;padding-left:6px">On-grade or elevated on<br>steel pedestals</p>
    <div class="cta cta--fire" style="left:188px;top:271px;width:108px;height:26px;font-size:13px">Learn more</div>
  </article>
</section>

</body>
</html>
```